Custom Beer Labelling Company Needs a Flyer

We need a flyer designed to promote Hopwrapz, a new company in Sydney that helps home brewers create their own small batch beer labels. Main purpose of the flyer is to increase awareness of the service we offer and drive traffic to the Hopwrapz shopify site - www.hopwrapz-example.com.au.
Our value proposition is about being easy (less than 5 minutes), affordable (full set of labels from only $12) with good quality (water resistant synthetic labels that remove cleanly).
The flyer should suit A4 printing and will preferably include screenshot of the "Create your Label" tool on the site, and/or examples of our label templates. It may also include other information from our site such eg from the "About Us" or About Our Labels" pages.

Target Market(s)

Home brewers, mostly males aged 20-50

Industry/Entity Type

It Company

Colors
ec1f27
fee3d4
f9ba93
f68d4e
f37122
f78f20
faa54b
fbc994
ffffff

Requirements
Must have
• Drive customers to www.hopwrapz-example.com as call to action
Nice to have
• screenshot(s) and examples of labels

```html
<!DOCTYPE html>
<html lang="en">
<head>
<meta charset="utf-8">
<title>Hopwrapz A4 Flyer</title>
<link href="https://fonts.googleapis.com/css2?family=Roboto:wght@300;400;500;700&family=Oswald:wght@500&display=swap" rel="stylesheet">
<style>
:root{
  --stage:#2e2e2e;
  --paper:#fffad6;
  --white:#ffffff;
  --orange:#f37122;
  --orange-soft:#f78f20;
  --peach:#fee3d4;
  --red:#ec1f27;
  --brown:#4a3322;
  --ink:#333333;
  --lime:#d7e022;
  --green:#5bb446;
  --yellow:#fff200;
  --black:#111111;
  --ui-grey:#777777;
  --ui-line:#cccccc;
}
*{box-sizing:border-box;margin:0;padding:0}
html,body{width:1200px;height:1000px;overflow:hidden}
body{background:var(--stage);font-family:"Roboto",Arial,sans-serif;position:relative}
.abs{position:absolute}
.flyer{left:270px;top:74px;width:660px;height:916px;background:var(--white)}
.paper{left:280px;top:84px;width:640px;height:896px;background:var(--paper)}

.brand{left:280px;top:92px;width:640px;height:92px;display:flex;align-items:center;justify-content:center;gap:16px}
.brand-mark{width:58px;height:58px;background:var(--orange)}
.brand-name{font-weight:700;font-size:66px;color:var(--brown);letter-spacing:1px;line-height:1}

.tagline-band{left:293px;top:195px;width:611px;height:47px;background:var(--orange);color:var(--white);font-size:16.5px;line-height:47px;text-align:center;white-space:nowrap;padding:0 10px}
.tagline-band b{font-weight:700}

.label-sample{width:92px;height:86px;border:1px solid #ddd}
.label-mint{background:linear-gradient(#eef3f1,#8cbcb5 40%,#8cbcb5 75%,#eef3f1)}
.label-khaki{background:linear-gradient(#f2efe4,#bdb492 40%,#bdb492 75%,#f2efe4)}
.label-black{background:linear-gradient(#eee,#111 20%,#111 85%,#eee)}

.arrow-banner{left:400px;top:255px;width:398px;height:32px}
.arrow-banner span{position:absolute;inset:0;display:flex;align-items:center;justify-content:center;color:var(--red);font-weight:700;font-size:13.5px}

.screen{left:400px;top:298px;width:398px;height:265px;background:var(--white);box-shadow:0 0 6px rgba(0,0,0,.35)}
.screen-logo{left:10px;top:14px;font-weight:700;font-size:16px;color:var(--brown)}
.screen-nav{left:180px;top:20px;width:212px;text-align:right;white-space:nowrap;font-size:6px;letter-spacing:.3px;color:var(--ui-grey)}
.screen-nav .on{color:var(--orange)}
.screen-bottle{left:7px;top:37px;width:186px;height:224px;background:linear-gradient(90deg,#4a0f12,#8c1c22 40%,#8c1c22 60%,#4a0f12)}
.screen-form{left:201px;top:40px;width:192px}
.form-title{font-weight:700;font-size:11px;color:#444}
.form-sub{font-size:6px;color:var(--ui-grey);margin-bottom:6px}
.form-grid{display:grid;grid-template-columns:1fr 1fr;gap:3px 8px}
.field label{display:block;font-size:5.5px;font-weight:700;color:#555;margin-bottom:1px}
.field div{border:1px solid var(--ui-line);height:13px;font-size:6.5px;padding:2px 3px;color:#444;white-space:nowrap;overflow:hidden}
.field.wide{grid-column:1/3}
.field.wide div{height:25px;font-size:6px;line-height:1.3;white-space:normal}
.swatches{display:flex;gap:3px;margin-top:2px}
.swatches i{width:13px;height:11px;display:block}
.price{font-size:10px;color:var(--ui-grey)}
.add-btn{background:var(--red);color:var(--white);font-size:6.5px;padding:3px 8px}

.offer-band{left:292px;top:568px;width:613px;height:42px;background:var(--green)}
.offer-band .title{left:50px;top:0;height:42px;line-height:42px;color:var(--white);font-size:20px;font-weight:500;white-space:nowrap}
.offer-price{left:770px;top:568px;width:135px;height:42px}
.offer-price span{position:absolute;left:26px;top:9px;color:var(--white);font-weight:700;font-size:18px;white-space:nowrap}
.offer-price small{font-size:7px;font-weight:400;margin-left:4px}

.intro{left:295px;top:624px;width:350px;font-size:13px;line-height:17.5px;color:var(--ink)}
.intro p{margin-bottom:17px}

.why{left:290px;top:793px;width:353px;height:131px;background:var(--peach);padding:14px 6px 0}
.why h2{font-family:"Oswald","Arial Narrow",sans-serif;font-weight:500;font-size:24px;text-align:center;color:var(--black);margin-bottom:12px}
.why p{font-size:10.5px;line-height:14px;color:var(--black);margin-bottom:10px}

.photo{left:651px;top:616px;width:254px;height:244px;background:linear-gradient(180deg,#c9c9cf,#8f8f96 45%,#3a1114)}
.quality-box{left:650px;top:866px;width:255px;height:52px;background:var(--yellow);display:flex;flex-direction:column;justify-content:center;text-align:center;font-weight:700;font-size:12px;line-height:16px;color:var(--black)}

.cta-band{left:280px;top:926px;width:640px;height:54px;background:var(--orange);color:var(--white);display:flex;align-items:center;justify-content:center;gap:28px;white-space:nowrap}
.cta-band .lead{font-size:26px;font-weight:300}
.cta-band .url{font-size:28px;font-weight:700}
</style>
</head>
<body>
<div class="abs flyer"></div>
<div class="abs paper"></div>

<header class="abs brand">
  <span class="brand-mark"></span>
  <span class="brand-name">Hopwrapz</span>
</header>

<div class="abs tagline-band">Easy &amp; affordable small batch beer labels at <b>www.hopwrapz-example.com.au</b></div>

<div class="abs label-sample label-mint" style="left:295px;top:255px" role="img" aria-label="Mint label template with laurel wreath"></div>
<div class="abs label-sample label-khaki" style="left:295px;top:364px" role="img" aria-label="Khaki label template with laurel wreath"></div>
<div class="abs label-sample label-black" style="left:295px;top:476px" role="img" aria-label="Black label template with laurel wreath"></div>
<div class="abs label-sample label-khaki" style="left:812px;top:255px" role="img" aria-label="Khaki label template with star icon"></div>
<div class="abs label-sample label-mint" style="left:812px;top:364px" role="img" aria-label="Mint label template with crown icon"></div>
<div class="abs label-sample label-black" style="left:812px;top:476px" role="img" aria-label="Black label template with crown icon"></div>

<div class="abs arrow-banner">
  <svg width="398" height="32" viewBox="0 0 398 32"><polygon points="16,0 382,0 398,16 382,32 16,32 0,16" fill="#d7e022"/></svg>
  <span>CREATE YOUR OWN LABEL IN LESS THAN 5 MINUTES</span>
</div>

<section class="abs screen">
  <div class="abs screen-logo">Hopwrapz</div>
  <div class="abs screen-nav">CREATE YOUR LABEL &nbsp;|&nbsp; <span class="on">ABOUT US</span> &nbsp;|&nbsp; ABOUT OUR LABELS &nbsp;|&nbsp; BLOG</div>
  <div class="abs screen-bottle" role="img" aria-label="Preview of a red beer bottle wearing a custom label"></div>
  <div class="abs screen-form">
    <div class="form-title">CREATE YOUR LABEL</div>
    <div class="form-sub">easy and affordable small batch beer labels</div>
    <div class="form-grid">
      <div class="field"><label>BEER NAME</label><div>Your Beer</div></div>
      <div class="field"><label>STYLE</label><div>Beer Style</div></div>
      <div class="field"><label>BREWED BY</label><div>Your Brewery</div></div>
      <div class="field"><label>TAGLINE</label><div>Your Tagline</div></div>
      <div class="field"><label>BREWED / BOTTLED</label><div>11/05/16 &nbsp; 21/05/16</div></div>
      <div class="field"><label>ABV</label><div>0.0%</div></div>
      <div class="field"><label>ORIGINAL GRAVITY</label><div>1.01</div></div>
      <div class="field"><label>FINAL GRAVITY</label><div>1.01</div></div>
      <div class="field wide"><label>NOTES</label><div>This may include further brewing details such as grain bill, mash and sparge temperatures, boil time and hop additions</div></div>
      <div class="field"><label>COLOR</label>
        <div class="swatches" style="border:0;padding:0"><i style="background:#111"></i><i style="background:#bdb492"></i><i style="background:#8cbcb5"></i><i style="background:#b3303c"></i></div>
      </div>
      <div class="field"><label>BOTTLE TYPE</label><div>Large &nbsp; Small</div></div>
    </div>
    <div style="display:flex;align-items:center;gap:40px;margin-top:6px;padding-left:24px">
      <span class="price">$0.79</span><span class="add-btn">ADD</span>
    </div>
  </div>
</section>

<div class="abs offer-band"><span class="abs title">FULL SET OF CUSTOM PRINTED LABELS</span></div>
<div class="abs offer-price">
  <svg width="135" height="42" viewBox="0 0 135 42"><polygon points="22,0 135,0 135,42 0,42" fill="#111111"/></svg>
  <span>$12USD<small>only</small></span>
</div>

<div class="abs intro">
  <p>Just fill in template with details of your brew, and select from our range of designs, colours, icons and bottle size.</p>
  <p>We print your labels in high quality LED on A4 sheets of die cut, self-adhesive labels.</p>
  <p>Our synthetic labels are water resistant and remove cleanly from your empties without tearing and without leftover glue crud.</p>
</div>

<section class="abs why">
  <h2>WHY HOPWRAPZ ?</h2>
  <p>The team at Hopwrapz have been enthusiastic home brewers for many years. We make some quite drinkable brews that we're proud to share.</p>
  <p>We want to bring your home brew out of the garage and onto the table.</p>
</section>

<div class="abs photo" role="img" aria-label="Photo of labelled home brew bottles around a steel keg"></div>
<div class="abs quality-box"><span>WATER RESISTANT</span><span>EASILY REMOVABLE SYNTHETIC LABELS</span></div>

<footer class="abs cta-band"><span class="lead">Visit Now</span><span class="url">www.hopwrapz-example.com.au</span></footer>
</body>
</html>
```